Redesign web application

we are a tele health start up. we need a new design for our platform that allows users, their family and docs to access their detailed stats online
users take readings using our wireless devices that transmit the readings to our server in the background All this happens in real time . and users can instantly login to the portal to view readings , make comments, , view charts,
if readings are not within in prescribed thresholds then alerts are reported on the website, SMS and email
please see the screenshots of existing pages
We need the following pages re designed
login page
patient DB summary , patient DB condition
Doc DB
Nurse DB
After you submit designs and we choose the winning design . please help to make minor modifications after that so that we can use it
Target Market(s)
Paying
Doctors/ Clinics/Clinic chains/ Specialists will be the ones who are paying for the service. the service
Non Paying
patients family members, doctors all will be accessing the system to view readings, alerts , make comments , see charts
Industry/Entity Type
Health
Colors
Look and feel

```html
<!DOCTYPE html>
<html lang="en">
<head>
<meta charset="utf-8">
<title>VitaWatch – Nurse Dashboard</title>
<link href="https://fonts.googleapis.com/css2?family=Open+Sans:wght@400;600&family=Varela+Round&display=swap" rel="stylesheet">
<style>
  :root{
    --green:#8cc63f;
    --green-dark:#6fac1f;
    --green-deep:#79b21c;
    --blue:#2a92d6;
    --orange:#f26522;
    --purple:#7b1f86;
    --purple-num:#7a2b8c;
    --text:#4a4a4a;
    --muted:#8c8c8c;
    --rule:#e2e2e2;
    --white:#ffffff;
  }
  *{margin:0;padding:0;box-sizing:border-box}
  html,body{width:1092px;height:1200px;overflow:hidden;background:var(--white)}
  body{position:relative;font-family:"Open Sans",Arial,sans-serif;color:var(--text)}
  .abs{position:absolute}
  h1,h2,h3{font-family:"Varela Round","Open Sans",sans-serif;font-weight:400}

  /* header */
  .brand{left:84px;top:32px;display:flex;align-items:center;gap:12px}
  .brand-dot{width:56px;height:56px;border-radius:50%;background:var(--green)}
  .brand-name{font-size:30px;font-weight:600;color:var(--green-dark);letter-spacing:1px}
  .partner{left:902px;top:36px;width:100px;height:28px;background:#f6f6f6;font-size:14px;font-weight:600;color:#222;display:flex;align-items:center;justify-content:center}
  .social{left:540px;top:77px;display:flex;gap:7px}
  .social span{width:22px;height:22px;background:#9aa3ad;border-radius:2px;display:block}
  .field{top:75px;width:142px;height:28px;border:1px solid #d6d6d6;background:#fafafa;font-size:11px;color:#666;padding:6px 11px}
  .field.user{left:633px}
  .field.pass{left:781px}
  .signup{left:927px;top:74px;width:75px;height:28px;background:var(--blue);color:#fff;font-size:11px;font-weight:600;display:flex;align-items:center;justify-content:center;letter-spacing:.3px}

  /* navigation */
  .nav{left:82px;top:121px;width:923px;height:47px;background:linear-gradient(#9dd14f,var(--green));border-radius:4px 4px 0 0;display:flex}
  .nav a{color:#fff;text-decoration:none;font-family:"Varela Round",sans-serif;font-size:16px;display:flex;align-items:center;justify-content:center;border-right:1px solid rgba(255,255,255,.35)}
  .nav a:last-child{border-right:none}

  .hero{left:82px;top:168px;width:923px;height:193px;background:linear-gradient(90deg,#e7e9ea 0%,#f3f4f4 25%,#cfd9e2 45%,#3b7cc4 60%,#e9ecee 75%,#2f6fc0 88%,#dfe3e6 100%)}

  /* welcome */
  .welcome{left:0;top:402px;width:1092px;text-align:center}
  .welcome h1{font-size:25px;color:#555}
  .welcome p{width:830px;margin:10px auto 0;font-size:11px;line-height:20px;color:var(--muted)}

  .hr{left:83px;top:539px;width:922px;height:1px;background:var(--rule)}
  .vr{top:540px;width:1px;height:320px;background:var(--rule)}

  /* columns */
  .patients{left:83px;top:576px;width:280px}
  .patients h2{font-size:22px;color:var(--green)}
  .patients p{font-size:11px;line-height:20px;color:var(--muted);margin-top:8px}
  .avatar{left:83px;top:664px;width:95px;height:89px;border-radius:4px;background:linear-gradient(#d9c19f,#efe2cf 60%,#a8c7e6)}
  .stats{left:191px;top:666px;list-style:none;font-size:12px}
  .stats li{height:27px}
  .stats b{color:var(--purple-num);font-weight:600;margin-right:6px}

  .reports{left:411px;top:578px;width:280px}
  .reports h2{font-size:22px;color:var(--orange)}
  .reports h2 small{font-size:14px}
  .report-list{list-style:none;margin-top:14px;font-size:12px}
  .report-list li{display:flex;justify-content:space-between;height:22.6px;padding-left:2px;padding-right:2px}

  .links{left:779px;top:576px}
  .links h2{font-size:22px;color:var(--purple)}
  .link-list{list-style:none;margin-top:10px;font-size:12px}
  .link-list li{height:25.5px;display:flex;align-items:center;gap:8px}
  .link-list svg{width:5px;height:9px}

  /* footer */
  .footer{left:0;top:924px;width:1092px;height:226px;background:linear-gradient(#94c43a,var(--green-deep))}
  .fcol{top:958px;color:#fff}
  .fcol h3{font-size:21px;margin-bottom:8px}
  .fcol ul{list-style:none;font-size:12px;font-weight:600;padding-left:3px}
  .fcol li{height:22.6px}
  .fcol li.phone{font-size:14px}
  .bottom{left:0;top:1150px;width:1092px;height:50px;background:var(--green-deep);color:#fff;font-size:12px;padding:17px 0 0 101px}
</style>
</head>
<body>

<header>
  <div class="abs brand"><span class="brand-dot"></span><span class="brand-name">VitaWatch</span></div>
  <div class="abs partner">PulseLink</div>
  <div class="abs social" aria-label="Social links"><span></span><span></span><span></span></div>
  <div class="abs field user">Username</div>
  <div class="abs field pass">Password</div>
  <div class="abs signup">SIGN UP</div>
</header>

<nav class="abs nav">
  <a style="width:103px">Home</a>
  <a style="width:107px">About Us</a>
  <a style="width:133px">Our Services</a>
  <a style="width:89px">Videos</a>
  <a style="width:156px">News &amp; Articles</a>
  <a style="width:132px">Locations</a>
  <a style="width:81px">Support</a>
  <a style="width:122px">Contact</a>
</nav>

<div class="abs hero" role="img" aria-label="Photo of nurses and doctors walking through a bright hospital corridor"></div>

<section class="abs welcome">
  <h1>Welcome to UAT Nurse</h1>
  <p>Vivamus porttitor g purus nisi eleifend libero a tempus libero lectus feugiat felis Morbi diam mauris viverra in gravida eu mattis in ante Morbi eget arcu Morbi porta libero id ullamcorper nonummy nibh ligula pulvinar metus eget consectetuer augue nisi quis lacus Ut ac mi quis lacus mollis aliquam Curabitur iaculis tempus eros Curabitur vel mi sit amet magna malesuada ultrices Ut nisi erat fermentum vel congue id euismod</p>
</section>

<div class="abs hr"></div>
<div class="abs vr" style="left:381px"></div>
<div class="abs vr" style="left:734px"></div>

<section class="abs patients">
  <h2>Monitored Patients</h2>
  <p>Etiam est nunc venenatis in tristique eu imperdiet ac nisl Cum sociis natoque penatibus et magnis</p>
</section>
<div class="abs avatar" role="img" aria-label="Portrait photo of the nurse"></div>
<ul class="abs stats">
  <li><b>14</b>Blood Glucose</li>
  <li><b>23</b>Blodd Pressure</li>
  <li><b>11</b>Body Weight</li>
</ul>

<section class="abs reports">
  <h2>JobStack Reports <small>(BP, BW &amp; BG)</small></h2>
  <ul class="report-list">
    <li><span>2 Consec Missed Reading (BP)</span><span>23</span></li>
    <li><span>3 Consec out of Threshold (BP)</span><span>05</span></li>
    <li><span>1 Week Missed Readings (BG)</span><span>05</span></li>
    <li><span>Normal Readings (BG)</span><span>04</span></li>
    <li><span>3 Consec Missed Reading (BW)</span><span>14</span></li>
    <li><span>Out of Threshold (BW)</span><span>10</span></li>
    <li><span>Review Date Reminder - 2 Days (BP)</span><span>12</span></li>
    <li><span>Completion Date Reminder - 7 Days (BP)</span><span>11</span></li>
    <li><span>Completion Date Reminder - 7 Days (BW)</span><span>04</span></li>
    <li><span>Completion Date Reminder - 7 Days (All)</span><span>21</span></li>
  </ul>
</section>

<section class="abs links">
  <h2>Links &amp; Resources</h2>
  <ul class="link-list">
    <li><svg viewBox="0 0 5 9"><path d="M0 0L5 4.5L0 9Z" fill="#ccc"/></svg>Etiam est nunc</li>
    <li><svg viewBox="0 0 5 9"><path d="M0 0L5 4.5L0 9Z" fill="#ccc"/></svg>Venenatis in tristique</li>
    <li><svg viewBox="0 0 5 9"><path d="M0 0L5 4.5L0 9Z" fill="#ccc"/></svg>Eu imperdiet ac nisl</li>
    <li><svg viewBox="0 0 5 9"><path d="M0 0L5 4.5L0 9Z" fill="#ccc"/></svg>Cum sociis natoque penatibus</li>
    <li><svg viewBox="0 0 5 9"><path d="M0 0L5 4.5L0 9Z" fill="#ccc"/></svg>Dis parturient montes</li>
  </ul>
</section>

<footer>
  <div class="abs footer"></div>
  <div class="abs fcol" style="left:96px"><h3>Quick Links</h3>
    <ul><li>About Us</li><li>Upcoming Events</li><li>Prayer Request</li><li>Donate</li></ul></div>
  <div class="abs fcol" style="left:268px"><h3>Services</h3>
    <ul><li>Phasellus felis dolor</li><li>Scelerisque tempus</li><li>Eget lobortis</li><li>Donec scelerisque</li></ul></div>
  <div class="abs fcol" style="left:458px"><h3>Our Locations</h3>
    <ul><li>45 W 71st Street #GA</li><li>New York</li><li class="phone">212.555.0148</li><li>info@carelinkhealth.org</li></ul></div>
  <div class="abs fcol" style="left:665px"><h3>Our Locations</h3>
    <ul><li>62 W 9th Street #AA</li><li>New York</li><li class="phone">212.555.0163</li><li>info@carelinkhealth.org</li></ul></div>
  <div class="abs bottom">© 2014 Company Name &nbsp;All right reserved &nbsp;Term of Use</div>
</footer>

</body>
</html>
```